Powerpoint master slides for business

Hello everyone,

I am looking for a new PowerPoint master slide that should be modern, slim and yet suitable for business.

I have uploaded a few pictures, which should serve as A. orientation for my presentation. A logo should be placed on the right-hand side of the cover sheet and all subsequent slides - please insert a placeholder here. Also attached are our company colors, which must be taken into account.

Basically, I would find 6 to 10 slides (cover sheet, classic slide, end, etc.) good.

PS: The slides are intended for general everyday work, ie the design should be subtle and easily adaptable to different situations, but still look chic, modern and classy.

```html
<!DOCTYPE html>
<html lang="en">
<head>
<meta charset="utf-8">
<title>Arlo Vent – Master Slides</title>
<link href="https://fonts.googleapis.com/css2?family=Mulish:wght@300;400;600;700;800&display=swap" rel="stylesheet">
<style>
  :root {
    --canvas: #808184;
    --navy: #1d3473;
    --orange: #e07b2a;
    --green: #9cc63b;
    --panel: #dcdddf;
    --white: #ffffff;
    --ink: #4a4d55;
    --grid: #e6e7ea;
  }
  * { margin: 0; padding: 0; box-sizing: border-box; }
  html, body { width: 1200px; height: 3914px; overflow: hidden; }
  body { background: var(--canvas); font-family: "Mulish", sans-serif; position: relative; }

  .slide { position: absolute; left: 99px; width: 1001px; height: 562px; overflow: hidden; }
  .slide--cover { top: 100px; }
  .slide--about { top: 717px; background: var(--panel); }
  .slide--solutions { top: 1335px; }
  .slide--services { top: 1952px; background: var(--panel); }
  .slide--chart { top: 2569px; background: var(--white); }
  .slide--closing { top: 3185px; }

  .photo { position: absolute; }
  .brand { position: absolute; right: 23px; top: 14px; font-weight: 700; font-size: 31px; color: var(--navy); letter-spacing: 0.2px; white-space: nowrap; }
  .brand--light { color: var(--white); }

  /* cover */
  .cover-photo { inset: 0; background: linear-gradient(100deg, #1a2733 0%, #22313f 45%, #2c3d4d 70%, #1b2530 100%); }
  .cover-title { position: absolute; left: 50%; top: 182px; transform: translateX(-50%); min-width: 251px; padding: 0 4px; white-space: nowrap; border-top: 2px solid var(--white); border-bottom: 2px solid var(--white); text-align: center; color: var(--white); font-weight: 700; font-size: 56px; line-height: 92px; }
  .cover-sub { position: absolute; left: 0; right: 0; top: 336px; text-align: center; color: var(--white); font-weight: 300; font-size: 42px; white-space: nowrap; }

  /* about */
  .about-photo { inset: 0; clip-path: polygon(0 0, 465px 0, 515px 100%, 0 100%); background: linear-gradient(160deg, #a98a6c 0%, #7d5a45 40%, #8c3c2c 60%, #c9c5c0 100%); }
  .section-title { position: absolute; font-weight: 700; font-size: 33px; color: var(--navy); white-space: nowrap; }
  .about-title { left: 570px; top: 128px; }
  .body-text { position: absolute; font-size: 14px; line-height: 19.8px; color: var(--ink); font-weight: 400; }
  .about-text { left: 570px; top: 187px; width: 378px; }

  /* solutions */
  .solutions-photo { inset: 0; background: linear-gradient(120deg, #dcdcd8 0%, #cfcbc4 35%, #b98e63 70%, #8a5c38 100%); }
  .solutions-title { left: 40px; top: 356px; }
  .solutions-text { left: 40px; top: 400px; width: 500px; color: #3e4047; }

  /* services */
  .services-photo { left: 0; top: 0; width: 100%; height: 281px; background: linear-gradient(90deg, #5b6670 0%, #7d8a94 40%, #9aa3a8 70%, #6d777f 100%); }
  .services-title { position: absolute; left: 0; right: 0; top: 102px; text-align: center; font-weight: 700; font-size: 31px; color: var(--white); }
  .card { position: absolute; top: 198px; width: 228px; height: 339px; background: var(--white); text-align: center; }
  .card:nth-of-type(1) { left: 24px; }
  .card:nth-of-type(2) { left: 268px; }
  .card:nth-of-type(3) { left: 510px; }
  .card:nth-of-type(4) { left: 754px; }
  .card-icon { position: absolute; left: 84px; top: 28px; width: 60px; height: 60px; }
  .card-title { position: absolute; left: 0; right: 0; top: 112px; font-weight: 800; font-size: 14px; color: #222; }
  .card-text { position: absolute; left: 24px; right: 24px; top: 146px; font-size: 11px; line-height: 13.3px; color: #555; }

  /* chart */
  .chart-band { position: absolute; left: 0; top: 0; width: 100%; height: 55px; background: var(--panel); }
  .chart-title { left: 0; right: 0; top: 84px; text-align: center; }
  .chart-text { left: 0; right: 0; top: 142px; text-align: center; color: #55585f; }
  .chart { position: absolute; left: 0; top: 0; width: 1001px; height: 562px; }
  .chart text { font-family: "Mulish", sans-serif; font-size: 8px; fill: #555; }

  /* closing */
  .closing-photo { inset: 0; background: linear-gradient(110deg, #24282b 0%, #2f3332 45%, #3a3a36 65%, #222527 100%); }
  .closing-brand { position: absolute; left: 0; right: 0; top: 124px; text-align: center; font-weight: 700; font-size: 40px; color: var(--white); white-space: nowrap; }
  .closing-thanks { position: absolute; left: 50%; top: 238px; transform: translateX(-50%); min-width: 280px; padding: 0 4px; white-space: nowrap; border-top: 2px solid var(--white); border-bottom: 2px solid var(--white); text-align: center; color: var(--white); font-weight: 300; font-size: 60px; line-height: 80px; }
  .contact { position: absolute; top: 486px; color: var(--white); font-size: 12px; line-height: 18px; white-space: nowrap; }
  .contact--call { right: 536px; text-align: right; }
  .contact--mail { left: 548px; }
  .contact-rule { position: absolute; top: 485px; width: 1px; height: 38px; background: var(--white); }
</style>
</head>
<body>

<section class="slide slide--cover">
  <div class="photo cover-photo" role="img" aria-label="Dark server room with a businessman holding a tablet"></div>
  <h1 class="cover-title">Arlo Vent</h1>
  <p class="cover-sub">Welcome to Arlo Vent</p>
</section>

<section class="slide slide--about">
  <div class="photo about-photo" role="img" aria-label="Man with glasses reading a document at a laptop in an office"></div>
  <div class="brand">Arlo Vent</div>
  <h2 class="section-title about-title">About us</h2>
  <p class="body-text about-text">Sed ut perspiciatis unde omnis iste natus error sit voluptatem accusantium doloremque laudantium, totam rem aperiam, eaque ipsa quae ab illo inventore veritatis et quasi architecto beatae vitae dicta sunt explicabo. Nemo enim ipsam voluptatem quia voluptas sit aspernatur aut odit aut fugit, sed quia consequuntur magni dolores eos qui ratione voluptatem sequi nesciunt. Neque porro quisquam est, qui dolorem ipsum quia dolor sit amet, consectetur, adipisci velit, sed quia non numquam eius modi tempora incidunt ut labore et dolore magnam aliquam quaerat voluptatem. Ut enim ad minima veniam, quis nostrum exercitationem ullam corporis suscipit laboriosam, nisi ut aliquid .</p>
</section>

<section class="slide slide--solutions">
  <div class="photo solutions-photo" role="img" aria-label="Hands typing on a laptop on a wooden desk"></div>
  <div class="brand">Arlo Vent</div>
  <h2 class="section-title solutions-title">Solutions</h2>
  <p class="body-text solutions-text">Sed ut perspiciatis unde omnis iste natus error sit voluptatem accusantium doloremque laudantium, totam rem aperiam, eaque ipsa quae ab illo inventore veritatis et quasi architecto beatae vitae dicta sunt explicabo. Nemo enim ipsam voluptatem quia voluptas sit aspernatur aut odit aut fugit, sed quia consequuntur magni dolores eos qui ratione voluptatem sequi nesciunt. Neque porro quisquam es.</p>
</section>

<section class="slide slide--services">
  <div class="photo services-photo" role="img" aria-label="Team of colleagues working at computers in a bright office"></div>
  <div class="brand brand--light">Arlo Vent</div>
  <h2 class="services-title">Services</h2>

  <article class="card">
    <svg class="card-icon" viewBox="0 0 60 60" fill="none" stroke="var(--orange)" stroke-width="2.5" stroke-linejoin="round">
      <circle cx="30" cy="14" r="8"/>
      <path d="M16 40 v-6 a14 10 0 0 1 28 0 v6"/>
      <rect x="18" y="34" width="24" height="16"/>
      <path d="M6 50 h48 l-6 -8 M6 50 l6 -8"/>
      <circle cx="30" cy="42" r="1" fill="var(--orange)"/>
    </svg>
    <h3 class="card-title">Lorem Ipsum</h3>
    <p class="card-text">Sed ut perspiciatis unde omnis iste natus error sit voluptatem accu antium doloremque laud antium, totam rem aperiam, eaque ipsa quae ab illo inventore veritatis et quasi architecto beatae vitae dicta sunt explicabo. Nemo enim ipsam voluptatem quia voluptas sit aspernatur aut odit aut fugit, sed quia consequuntur magni dolores eos qui ratione voluptatem sequi nesciunt.</p>
  </article>

  <article class="card">
    <svg class="card-icon" viewBox="0 0 60 60" fill="none" stroke="var(--orange)" stroke-width="2.5" stroke-linejoin="round">
      <path d="M14 8 h22 l10 10 v36 h-32 z"/>
      <path d="M10 12 v46 h30"/>
      <path d="M6 16 v46"/>
      <circle cx="30" cy="36" r="6"/>
      <path d="M30 26 v4 M30 42 v4 M20 36 h4 M36 36 h4"/>
    </svg>
    <h3 class="card-title">Lorem Ipsum</h3>
    <p class="card-text">Sed ut perspiciatis unde omnis iste natus error sit voluptatem accu antium doloremque laud antium, totam rem aperiam, eaque ipsa quae ab illo inventore veritatis et quasi architecto beatae vitae dicta sunt explicabo. Nemo enim ipsam voluptatem quia voluptas sit aspernatur aut odit aut fugit, sed quia consequuntur magni dolores eos qui ratione voluptatem sequi nesciunt.</p>
  </article>

  <article class="card">
    <svg class="card-icon" viewBox="0 0 60 60" fill="none" stroke="var(--orange)" stroke-width="2.5" stroke-linejoin="round">
      <path d="M38 54 h-26 v-48 h22 l10 10 v16"/>
      <path d="M34 6 v10 h10"/>
      <path d="M18 20 h12 M18 28 h20 M18 36 h14"/>
      <path d="M34 54 l4 -10 l14 -14 l6 6 l-14 14 z"/>
    </svg>
    <h3 class="card-title">Lorem Ipsum</h3>
    <p class="card-text">Sed ut perspiciatis unde omnis iste natus error sit voluptatem accu antium doloremque laud antium, totam rem aperiam, eaque ipsa quae ab illo inventore veritatis et quasi architecto beatae vitae dicta sunt explicabo. Nemo enim ipsam voluptatem quia voluptas sit aspernatur aut odit aut fugit, sed quia consequuntur magni dolores eos qui ratione voluptatem sequi nesciunt.</p>
  </article>

  <article class="card">
    <svg class="card-icon" viewBox="0 0 60 60" fill="none" stroke="var(--orange)" stroke-width="2.5" stroke-linejoin="round">
      <rect x="6" y="34" width="20" height="20"/>
      <path d="M26 6 h28 v28" stroke-dasharray="5 4"/>
      <path d="M26 34 l22 -22 M36 12 h12 v12"/>
    </svg>
    <h3 class="card-title">Lorem Ipsum</h3>
    <p class="card-text">Sed ut perspiciatis unde omnis iste natus error sit voluptatem accu antium doloremque laud antium, totam rem aperiam, eaque ipsa quae ab illo inventore veritatis et quasi architecto beatae vitae dicta sunt explicabo. Nemo enim ipsam voluptatem quia voluptas sit aspernatur aut odit aut fugit, sed quia consequuntur magni dolores eos qui ratione voluptatem sequi nesciunt.</p>
  </article>
</section>

<section class="slide slide--chart">
  <div class="chart-band"></div>
  <div class="brand">Arlo Vent</div>
  <h2 class="section-title chart-title">Lorem ipsum dolor</h2>
  <p class="body-text chart-text">Sed ut perspiciatis unde omnis iste natus error sit voluptatem accusantium doloremque laudantium, totam rem aperiam,<br>eaque ipsa quae ab illo inventore veritatis et quasi architecto beatae vitae dicta sunt explicabo.</p>

  <svg class="chart" viewBox="0 0 1001 562" aria-label="Monthly line chart with two series">
    <g stroke="var(--grid)" stroke-width="1">
      <line x1="106" y1="222" x2="934" y2="222"/><line x1="106" y1="250" x2="934" y2="250"/>
      <line x1="106" y1="278" x2="934" y2="278"/><line x1="106" y1="306" x2="934" y2="306"/>
      <line x1="106" y1="334" x2="934" y2="334"/><line x1="106" y1="363" x2="934" y2="363"/>
      <line x1="106" y1="391" x2="934" y2="391"/><line x1="106" y1="419" x2="934" y2="419"/>
      <line x1="106" y1="447" x2="934" y2="447"/><line x1="106" y1="475" x2="934" y2="475"/>
      <line x1="106" y1="503" x2="934" y2="503"/>
      <line x1="106" y1="222" x2="106" y2="503"/><line x1="175" y1="222" x2="175" y2="503"/>
      <line x1="244" y1="222" x2="244" y2="503"/><line x1="313" y1="222" x2="313" y2="503"/>
      <line x1="382" y1="222" x2="382" y2="503"/><line x1="451" y1="222" x2="451" y2="503"/>
      <line x1="520" y1="222" x2="520" y2="503"/><line x1="589" y1="222" x2="589" y2="503"/>
      <line x1="658" y1="222" x2="658" y2="503"/><line x1="727" y1="222" x2="727" y2="503"/>
      <line x1="796" y1="222" x2="796" y2="503"/><line x1="865" y1="222" x2="865" y2="503"/>
      <line x1="934" y1="222" x2="934" y2="503"/>
    </g>
    <g text-anchor="end">
      <text x="98" y="225">100</text><text x="98" y="253">90</text><text x="98" y="281">80</text>
      <text x="98" y="309">70</text><text x="98" y="337">60</text><text x="98" y="366">50</text>
      <text x="98" y="394">40</text><text x="98" y="422">30</text><text x="98" y="450">20</text>
      <text x="98" y="478">10</text><text x="98" y="506">0</text>
    </g>
    <g text-anchor="middle">
      <text x="140" y="523">JAN</text><text x="209" y="523">FEB</text><text x="278" y="523">MAR</text>
      <text x="347" y="523">APR</text><text x="416" y="523">MAY</text><text x="485" y="523">JUN</text>
      <text x="554" y="523">JUL</text><text x="623" y="523">AUG</text><text x="692" y="523">SEP</text>
      <text x="761" y="523">OCT</text><text x="830" y="523">NOV</text><text x="899" y="523">DEC</text>
    </g>
    <polyline fill="none" stroke="var(--green)" stroke-width="2" points="106,391 175,363 244,391 313,306 382,306 451,334 520,306 589,306 658,261 727,250 796,250 865,261 934,250"/>
    <g fill="var(--green)">
      <circle cx="106" cy="391" r="3"/><circle cx="175" cy="363" r="3"/><circle cx="244" cy="391" r="3"/>
      <circle cx="313" cy="306" r="3"/><circle cx="382" cy="306" r="3"/><circle cx="451" cy="334" r="3"/>
      <circle cx="520" cy="306" r="3"/><circle cx="589" cy="306" r="3"/><circle cx="658" cy="261" r="3"/>
      <circle cx="727" cy="250" r="3"/><circle cx="796" cy="250" r="3"/><circle cx="865" cy="261" r="3"/>
      <circle cx="934" cy="250" r="3"/>
    </g>
    <polyline fill="none" stroke="var(--orange)" stroke-width="2" points="106,475 175,419 244,447 313,363 382,334 451,391 520,363 589,391 727,278 865,334 934,278"/>
    <g fill="var(--orange)">
      <circle cx="106" cy="475" r="3"/><circle cx="175" cy="419" r="3"/><circle cx="244" cy="447" r="3"/>
      <circle cx="313" cy="363" r="3"/><circle cx="382" cy="334" r="3"/><circle cx="451" cy="391" r="3"/>
      <circle cx="520" cy="363" r="3"/><circle cx="589" cy="391" r="3"/><circle cx="727" cy="278" r="3"/>
      <circle cx="865" cy="334" r="3"/><circle cx="934" cy="278" r="3"/>
    </g>
  </svg>
</section>

<section class="slide slide--closing">
  <div class="photo closing-photo" role="img" aria-label="Dimmed open-plan office with people at desks"></div>
  <div class="closing-brand">Arlo Vent</div>
  <div class="closing-thanks">Thank You</div>
  <p class="contact contact--call">Call Us<br>+1 555 010 0199</p>
  <span class="contact-rule" style="left:474px"></span>
  <span class="contact-rule" style="left:534px"></span>
  <p class="contact contact--mail">Emai Us<br>info@arlovent.com</p>
</section>

</body>
</html>
```